Brightwire Hollow Business cards

one side I would like my logo (uploaded) and the other side I want my details. I'm an electrician in sydney. The logo side I'm happy with just a white background and our logo in the middle.

Details for other side
24/7 Sydney Electrician
Marcus Pell
0431 587 219
marcus@brightwirehollow.com.au
brightwirehollow.com.au
icons for facebook, instagram, linked in

Industry/Entity Type

electrician

Contact Information for Business Card

company info

```html
<!DOCTYPE html>
<html lang="en">
<head>
<meta charset="utf-8">
<title>Brightwire Hollow – Business Cards</title>
<link rel="stylesheet" href="https://fonts.googleapis.com/css2?family=Montserrat:wght@500;600;700&display=swap">
<style>
  :root {
    --red: #ee3524;
    --ink: #111111;
    --paper: #ffffff;
    --backdrop: #bdbdbd;
    --rule: #d9a7a2;
  }
  * { box-sizing: border-box; margin: 0; padding: 0; }
  html, body { width: 1200px; height: 800px; overflow: hidden; }
  body {
    background: var(--backdrop);
    font-family: "Montserrat", sans-serif;
    display: flex;
    align-items: center;
    justify-content: center;
    gap: 40px;
  }
  .card {
    position: relative;
    width: 540px;
    height: 309px;
    background: var(--paper);
    border-radius: 16px;
    border-bottom: 3px solid var(--red);
    overflow: hidden;
    box-shadow: 0 14px 30px rgba(0,0,0,0.25);
  }

  /* Details side */
  .card-details .corner-tab {
    position: absolute;
    top: 0; right: 30px;
    width: 26px; height: 64px;
    background: var(--ink);
  }
  .card-details .holder-name {
    position: absolute;
    left: 36px; top: 78px;
    color: var(--red);
    font-weight: 600;
    font-size: 22px;
    letter-spacing: 1px;
    text-transform: uppercase;
  }
  .card-details .contact-band {
    position: absolute;
    left: 0; top: 122px;
    width: 340px; height: 100px;
    background: var(--red);
    padding: 12px 0 0 32px;
    display: flex;
    flex-direction: column;
    gap: 6px;
  }
  .contact-line {
    display: flex;
    align-items: center;
    gap: 10px;
    color: var(--paper);
    font-weight: 500;
    font-size: 15px;
  }
  .contact-line svg { width: 20px; height: 20px; flex: none; }
  .card-details .tagline {
    position: absolute;
    left: 36px; top: 248px;
    color: var(--ink);
    font-weight: 600;
    font-size: 15px;
    letter-spacing: 0.5px;
    text-transform: uppercase;
  }
  .card-details .brand-name {
    position: absolute;
    left: 360px; top: 110px;
    width: 160px;
    color: var(--red);
    font-weight: 700;
    font-size: 24px;
    line-height: 1.1;
    text-transform: uppercase;
  }

  /* Logo side */
  .card-logo {
    display: flex;
    flex-direction: column;
    align-items: center;
    justify-content: center;
  }
  .card-logo .brand-name {
    color: var(--red);
    font-weight: 700;
    font-size: 40px;
    letter-spacing: 1px;
    text-transform: uppercase;
    margin-bottom: 28px;
  }
  .social-row {
    display: flex;
    align-items: center;
    gap: 10px;
    width: 420px;
  }
  .social-row .rule { flex: 1; height: 1px; background: var(--rule); }
  .social-row .social-dot {
    width: 24px; height: 24px;
    border: 1.5px solid var(--red);
    border-radius: 50%;
  }
</style>
</head>
<body>
  <section class="card card-details">
    <div class="corner-tab"></div>
    <h1 class="holder-name">Marcus Pell</h1>
    <div class="contact-band">
      <div class="contact-line">
        <svg viewBox="0 0 20 20"><circle cx="10" cy="10" r="9" fill="none" stroke="#fff" stroke-width="1.4"/><path d="M7 6l2 2-1 1.2a6 6 0 0 0 2.8 2.8L12 11l2 2-1.3 1.3C9.5 14 6 10.5 5.7 7.3z" fill="#fff"/></svg>
        <span>0431 587 219</span>
      </div>
      <div class="contact-line">
        <svg viewBox="0 0 20 20"><circle cx="10" cy="10" r="9" fill="none" stroke="#fff" stroke-width="1.4"/><rect x="5.5" y="7" width="9" height="6.5" fill="none" stroke="#fff" stroke-width="1.2"/><path d="M5.5 7l4.5 3.5L14.5 7" fill="none" stroke="#fff" stroke-width="1.2"/></svg>
        <span>marcus@brightwirehollow.com.au</span>
      </div>
      <div class="contact-line">
        <svg viewBox="0 0 20 20"><circle cx="10" cy="10" r="9" fill="none" stroke="#fff" stroke-width="1.4"/><circle cx="10" cy="10" r="5" fill="none" stroke="#fff" stroke-width="1.1"/><path d="M5 10h10M10 5c-2 3-2 7 0 10M10 5c2 3 2 7 0 10" fill="none" stroke="#fff" stroke-width="1"/></svg>
        <span>brightwirehollow.com.au</span>
      </div>
    </div>
    <p class="tagline">24/7 Sydney Electrician</p>
    <p class="brand-name">Brightwire Hollow</p>
  </section>

  <section class="card card-logo">
    <p class="brand-name">Brightwire Hollow</p>
    <div class="social-row" aria-label="Social media links">
      <span class="rule"></span>
      <span class="social-dot"></span>
      <span class="social-dot"></span>
      <span class="social-dot"></span>
      <span class="rule"></span>
    </div>
  </section>
</body>
</html>
```